New Ophthalmic surgical website with a fresh clean modern, less is more look, with multiple category product lines (maybe a modern look and animated picture for each category) where we can continually add new products to the website ourselves, each with individual catalogue numbers, photos, and descriptions, eventually being able to order products from the website itself. Original setup is mostly just PDFs catalogs of our current products.
Preliminary Categories for updated website
Corvanta-Medix.com :
BLADES
Diamond
Slit Knives
Sapphire
Paracentisis
Disposable
Reusable
CANNULAS
Plexura Posterior Seg Disp
Corvanta Medix Anterior Seg Disp
Talvor reusable
DRY EYE SUITE
Brightwell Lumen Analytics
Amniotic Drops
OcuFlent
Dune & Frost Wrap
Marlow Nutrient
Intraductal Meibomian Gland Probes/Tubes
Talvor Dry Eye Booklet
Talvor Meibum Expressor Forceps
TALVOR Instruments
Full Catalogue
Algerbrushes
Cannulas
Canaloplasty Set
Diamond Knives
Dry Eye Booklet
Eco Single Use Instruments
RETINA
PELLANT Laser Probes
Plexura Disp Cannulas
Plexura Disp Forceps
Brisk Lenses
Marlow Nutrients
Corvanta Medix ILM Forceps
GLAUCOMA
Quill Sterile Patch Grafts
PELLANT G6
Talvor Instruments
Talvor Canaloplasty Set
Brisk Lenses
LASIK
Talvor Instruments
Talvor Refractive Instruments
CORNEA
Quill Sterile Cornea
Tamsel OptiTrust
Amniotic Drops
Talvor Instruments
CATARACT
Femto Instruments
Talvor Instruments
Talvor Diamond Knives
Corvanta Medix Disp Cannulas
Marden Choppers
Toric Markers
Sterilization Products
SteroPak Autoclaves
Sterilization Trays
Room Sterilizers
SUTURE
Target Market(s)
Ophthalmology surgery centers & hospitals, ophthalmology offices and Optometric offices. Customers are the eye doctors and eye nurses that use and order the products
Number of Pages Required
5+ page
Look and feel

```html
<!DOCTYPE html>
<html lang="en">
<head>
<meta charset="utf-8">
<title>Corvanta Medix — Ophthalmic Surgical</title>
<link rel="stylesheet" href="https://fonts.googleapis.com/css2?family=Nunito+Sans:wght@300;400;600;700&display=swap">
<style>
:root{
  --teal:#12a89b;
  --teal-dark:#127a93;
  --teal-mint:#1fd3a3;
  --ink:#3c3c3c;
  --muted:#8a8a8a;
  --grey-band:#e8e8e8;
  --footer:#f3f3f3;
  --white:#ffffff;
  --skin:#d79c86;
  --skin-light:#efd2c2;
  --glove:#3f82d6;
  --coat:#f4f5f5;
}
*{box-sizing:border-box;margin:0;padding:0}
html,body{width:1200px;height:2497px;overflow:hidden}
body{position:relative;background:var(--white);font-family:"Nunito Sans",Arial,sans-serif;color:var(--ink)}
.abs{position:absolute}

/* header */
.site-header{left:0;top:0;width:1200px;height:103px;background:var(--white)}
.brand{left:140px;top:34px;font-size:33px;font-weight:600;color:var(--teal);letter-spacing:.2px}
.nav a{position:absolute;top:42px;font-size:16px;color:#4a4a4a;text-decoration:none;letter-spacing:.5px}
.nav a.active{color:var(--teal)}
.nav .underline{position:absolute;left:482px;top:97px;width:66px;height:5px;background:var(--teal)}

/* hero */
.hero{left:0;top:103px;width:1200px;height:483px;background:
  radial-gradient(ellipse 230px 250px at 64% 48%,rgba(212,146,124,.97),rgba(212,146,124,0) 72%),
  radial-gradient(ellipse 150px 110px at 78% 30%,rgba(232,232,230,.95),rgba(232,232,230,0) 75%),
  radial-gradient(ellipse 220px 110px at 72% 100%,rgba(160,192,205,.95),rgba(160,192,205,0) 75%),
  radial-gradient(ellipse 190px 200px at 47% 38%,rgba(240,228,206,.98),rgba(240,228,206,0) 72%),
  radial-gradient(ellipse 170px 140px at 30% 70%,rgba(236,222,200,.9),rgba(236,222,200,0) 72%),
  radial-gradient(ellipse 230px 380px at 6% 55%,var(--coat),rgba(244,245,245,0) 75%),
  linear-gradient(90deg,#e4e9eb,#dce2e4 50%,#edf0f1)}
.hero-kicker{left:138px;top:283px;width:428px;height:45px;background:rgba(255,255,255,.88);color:var(--teal);font-size:27.5px;font-weight:700;padding:8px 18px;letter-spacing:.4px}
.hero-title{left:138px;top:330px;width:428px;height:56px;background:var(--teal);color:var(--white);font-size:37.5px;font-weight:600;padding:4px 18px;letter-spacing:.6px}
.dots{left:588px;top:557px;display:flex;gap:8px}
.dots span{width:15px;height:15px;border-radius:50%;background:var(--white);border:2px solid var(--white)}
.dots span:first-child{background:transparent}

/* welcome */
.welcome-photo{left:574px;top:586px;width:460px;height:396px;background:
  radial-gradient(ellipse 60px 70px at 16% 8%,rgba(63,130,214,.95),rgba(63,130,214,0) 75%),
  radial-gradient(ellipse 80px 80px at 25% 100%,rgba(63,130,214,.9),rgba(63,130,214,0) 75%),
  radial-gradient(ellipse 70px 90px at 78% 95%,rgba(63,130,214,.95),rgba(63,130,214,0) 75%),
  radial-gradient(ellipse 70px 110px at 85% 30%,rgba(176,120,80,.85),rgba(176,120,80,0) 75%),
  radial-gradient(ellipse 140px 200px at 60% 52%,var(--skin-light),rgba(239,210,194,0) 80%),
  radial-gradient(ellipse 130px 130px at 8% 40%,#f2f2f2,rgba(242,242,242,0) 80%),
  linear-gradient(90deg,#ffffff 0%,#ffffff 18%,#f7ede6 45%,#ffffff 100%)}
.welcome-title{left:150px;top:655px;font-size:32px;font-weight:400;color:#444}
.welcome-text{left:150px;top:708px;width:480px;font-size:14.5px;line-height:27px;color:#555}
.welcome-text p+p{margin-top:6px}
.btn{display:block;text-align:center;color:var(--white);font-weight:700;font-size:11px;letter-spacing:.5px;text-decoration:none}
.btn-welcome{left:146px;top:874px;width:115px;height:35px;line-height:35px;border-radius:3px;background:linear-gradient(#1a8fa3,var(--teal-dark));box-shadow:0 2px 3px rgba(0,0,0,.25)}

/* features */
.features{left:0;top:982px;width:1200px;height:421px;background:var(--grey-band)}
.card{position:absolute;top:63px;width:283px;height:276px;background:var(--white);text-align:center}
.card-photo{width:283px;height:160px}
.photo-surgery{background:
  radial-gradient(ellipse 60px 40px at 45% 62%,rgba(230,140,60,.9),rgba(230,140,60,0) 75%),
  radial-gradient(ellipse 120px 60px at 30% 25%,rgba(120,160,220,.9),rgba(120,160,220,0) 75%),
  linear-gradient(135deg,#22385c,#3a5f95 45%,#141f33)}
.photo-technology{background:
  radial-gradient(ellipse 70px 60px at 45% 40%,rgba(70,80,90,.85),rgba(70,80,90,0) 75%),
  radial-gradient(ellipse 60px 50px at 82% 55%,rgba(226,178,156,.95),rgba(226,178,156,0) 75%),
  linear-gradient(180deg,#2a2e38 0%,#c8ccd1 22%,#e9ebee 70%,#f3f1ef)}
.photo-mission{background:
  radial-gradient(ellipse 70px 70px at 25% 45%,rgba(232,190,165,.95),rgba(232,190,165,0) 75%),
  radial-gradient(ellipse 80px 80px at 75% 45%,rgba(226,176,150,.95),rgba(226,176,150,0) 75%),
  radial-gradient(ellipse 70px 40px at 15% 100%,rgba(40,150,200,.95),rgba(40,150,200,0) 75%),
  linear-gradient(90deg,#6b4131,#9a6a55 50%,#5a3426)}
.card h3{margin-top:15px;font-size:23px;font-weight:400;color:var(--teal-dark)}
.card p{margin:6px auto 0;width:230px;font-size:11.5px;line-height:15px;color:var(--muted)}
.card .btn{position:absolute;left:79px;top:258px;width:125px;height:31px;line-height:31px;border-radius:16px;background:var(--teal-dark)}
.card .btn.mint{background:var(--teal-mint)}

/* services */
.services{left:0;top:1403px;width:1200px;height:391px;background:linear-gradient(110deg,#0f8592 0%,#0fa79c 50%,#08d59a 100%);overflow:hidden}
.services h2{position:absolute;left:0;top:38px;width:1200px;text-align:center;color:var(--white);font-size:31px;font-weight:400}
.service{position:absolute;top:86px;width:234px;height:234px;border-radius:50%;background:rgba(10,110,120,.16);border:2px solid rgba(255,255,255,.12);text-align:center;color:var(--white)}
.service svg{position:absolute;left:77px;top:38px}
.service h4{position:absolute;left:0;top:135px;width:100%;font-size:21px;font-weight:400;letter-spacing:.5px}
.service .btn{position:absolute;left:59px;top:182px;width:117px;height:27px;line-height:27px;border-radius:14px;background:rgba(0,90,100,.28);font-size:10.5px}
.arrow{position:absolute;top:196px}

/* blogs */
.blogs-title{left:135px;top:1852px;font-size:31px;font-weight:400;color:#444}
.blog{position:absolute;top:1915px;width:470px;height:160px}
.blog-photo{position:absolute;left:0;top:0;width:204px;height:153px}
.photo-blog-surgery{background:
  radial-gradient(ellipse 50px 40px at 55% 70%,rgba(220,120,50,.9),rgba(220,120,50,0) 75%),
  radial-gradient(ellipse 70px 50px at 30% 20%,rgba(170,180,190,.9),rgba(170,180,190,0) 75%),
  linear-gradient(135deg,#2f4660,#56657a 50%,#1e2a38)}
.photo-blog-exam{background:
  radial-gradient(ellipse 60px 50px at 50% 60%,rgba(226,178,150,.95),rgba(226,178,150,0) 75%),
  radial-gradient(ellipse 60px 40px at 15% 95%,rgba(90,170,230,.95),rgba(90,170,230,0) 75%),
  linear-gradient(180deg,#3a4450 0%,#9aa4ae 35%,#dfe6ec 100%)}
.blog-body{position:absolute;left:224px;top:0;width:230px}
.blog-body h3{font-size:17px;font-weight:400;color:var(--teal-dark);margin-top:-2px}
.blog-body p{margin-top:7px;font-size:11.5px;line-height:20px;color:var(--muted)}
.blog-body a{display:block;margin-top:8px;font-size:13px;color:var(--teal);text-decoration:none;letter-spacing:.3px}

/* footer */
.site-footer{left:0;top:2160px;width:1200px;height:337px;background:var(--footer)}
.fcol{position:absolute;top:52px}
.fcol h5{font-size:18px;font-weight:400;color:#333;border-left:3px solid var(--teal);padding-left:8px;line-height:26px;margin-left:-11px}
.fcol ul{list-style:none;margin-top:10px}
.fcol li{font-size:13px;line-height:30px;color:#666}
.fcol address{font-style:normal;margin-top:12px;font-size:13px;line-height:21px;color:#666}
.fcol address .gap{margin-top:8px}
.socials{display:flex;gap:5px;margin-top:10px;margin-left:2px}
.socials span{width:33px;height:33px;border-radius:50%}
.footer-rule{left:150px;top:2436px;width:912px;height:1px;background:#d6d6d6}
.copyright{left:0;top:2455px;width:1200px;text-align:center;font-size:11.5px;color:#666}
</style>
</head>
<body>

<header class="abs site-header">
  <div class="abs brand">Corvanta Medix</div>
  <nav class="nav">
    <a class="active" style="left:489px">HOME</a>
    <a style="left:578px">ABOUT US</a>
    <a style="left:697px">BLOGS</a>
    <a style="left:792px">SERVICES</a>
    <a style="left:904px">NEWS</a>
    <a style="left:991px">CONTACT</a>
    <span class="underline"></span>
  </nav>
</header>

<section class="abs hero" role="img" aria-label="Clinician in a white coat applying eye drops to an older patient's eye"></section>
<div class="abs hero-kicker">OPHTHALMIC SURGICAL</div>
<div class="abs hero-title">PROIN NULLA ARCU</div>
<div class="abs dots"><span></span><span></span><span></span><span></span></div>

<section class="welcome">
  <div class="abs welcome-photo" role="img" aria-label="Patient with closed eyes receiving a treatment from blue-gloved hands"></div>
  <h1 class="abs welcome-title">Welcome to Corvanta Medix</h1>
  <div class="abs welcome-text">
    <p>consectetuer augue nisi quis lacus Ut ac mi quis lacus mollis aliquam<br>Curabitur iaculis tempus eros Curabitur vel mi sit amet</p>
    <p>ultrices Ut nisi erat fermentum vel congue id euismod in elit Fusce<br>ultricies orci ac feugiat suscipit leo massa sodales velit et scelerisque mi<br>tortor at r mauris ipsum iaculis elit congue gra</p>
  </div>
  <a class="abs btn btn-welcome">READ MORE</a>
</section>

<section class="abs features">
  <div class="card" style="left:151px">
    <div class="card-photo photo-surgery" role="img" aria-label="Surgeon operating under a microscope"></div>
    <h3>Why We Are</h3>
    <p>sociosqu ad litora torquent per conubia nostra per inceptos hymenaeos</p>
    <a class="btn">READ MORE</a>
  </div>
  <div class="card" style="left:456px">
    <div class="card-photo photo-technology" role="img" aria-label="Technician using an ophthalmic diagnostic device"></div>
    <h3>Our Technology</h3>
    <p>sociosqu ad litora torquent per conubia nostra per inceptos hymenaeos</p>
    <a class="btn">READ MORE</a>
  </div>
  <div class="card" style="left:760px">
    <div class="card-photo photo-mission" role="img" aria-label="Eye doctor examining a patient with an ophthalmoscope"></div>
    <h3>Our Mission</h3>
    <p>sociosqu ad litora torquent per conubia nostra per inceptos hymenaeos</p>
    <a class="btn mint">READ MORE</a>
  </div>
</section>

<section class="abs services">
  <h2>Our Services</h2>
  <svg class="arrow" style="left:108px" width="20" height="32" viewBox="0 0 20 32"><path d="M16 3 L4 16 L16 29" fill="none" stroke="rgba(255,255,255,.8)" stroke-width="3"/></svg>
  <svg class="arrow" style="left:1072px" width="20" height="32" viewBox="0 0 20 32"><path d="M4 3 L16 16 L4 29" fill="none" stroke="rgba(255,255,255,.8)" stroke-width="3"/></svg>

  <div class="service" style="left:150px">
    <svg width="80" height="84" viewBox="0 0 80 84" fill="none" stroke="#fff" stroke-width="2.5" stroke-linecap="round"><path d="M64 6 L22 56 L12 72 L28 64 L70 14 Z"/><path d="M22 56 L30 62"/><path d="M40 76 H78" stroke-dasharray="2 4"/></svg>
    <h4>BLADES</h4>
    <a class="btn">READ MORE</a>
  </div>
  <div class="service" style="left:375px">
    <svg width="80" height="84" viewBox="0 0 80 84" fill="none" stroke="#fff" stroke-width="2.5" stroke-linecap="round"><path d="M62 6 L34 46"/><path d="M70 12 L42 52"/><path d="M28 44 L46 58"/><path d="M36 50 L22 70 L18 76"/><path d="M30 58 L24 52"/></svg>
    <h4>CANNULAS</h4>
    <a class="btn">READ MORE</a>
  </div>
  <div class="service" style="left:600px">
    <svg width="80" height="84" viewBox="0 0 80 84" fill="none" stroke="#fff" stroke-width="2.5"><path d="M2 42 Q40 6 78 42 Q40 78 2 42 Z"/><circle cx="40" cy="42" r="15"/><circle cx="40" cy="42" r="7"/></svg>
    <h4>DRY EYE SUITE</h4>
    <a class="btn">READ MORE</a>
  </div>
  <div class="service" style="left:825px">
    <svg width="80" height="84" viewBox="0 0 80 84" fill="none" stroke="#fff" stroke-width="2.5"><circle cx="40" cy="40" r="30"/><path d="M20 24 Q34 40 20 56"/><path d="M20 24 Q10 40 20 56"/><path d="M40 40 H70 M54 28 Q60 40 54 52"/></svg>
    <h4>RETINA</h4>
    <a class="btn">READ MORE</a>
  </div>
</section>

<section class="blogs">
  <h2 class="abs blogs-title">Our Blogs</h2>
  <article class="blog" style="left:135px">
    <div class="blog-photo photo-blog-surgery" role="img" aria-label="Eye surgery in progress under a surgical microscope"></div>
    <div class="blog-body">
      <h3>Blog Tittle here</h3>
      <p>sociosqu ad litora torquent per conubia<br>nostra per inceptos hymenaeos Proin<br>nulla sociosqu ad litora torquent per<br>conubia nostra per inceptos hymenaeos<br>Proin nulla arcu nonummy</p>
      <a>READ MORE</a>
    </div>
  </article>
  <article class="blog" style="left:611px">
    <div class="blog-photo photo-blog-exam" role="img" aria-label="Patient at an eye examination instrument"></div>
    <div class="blog-body">
      <h3>Blog Tittle here</h3>
      <p>sociosqu ad litora torquent per conubia<br>nostra per inceptos hymenaeos Proin<br>nulla sociosqu ad litora torquent per<br>conubia nostra per inceptos hymenaeos<br>Proin nulla arcu nonummy</p>
      <a>READ MORE</a>
    </div>
  </article>
</section>

<footer class="abs site-footer">
  <div class="fcol" style="left:148px">
    <h5>INFORMATION</h5>
    <ul><li>Home</li><li>About Us</li><li>Why Choose Us</li><li>Our Products</li></ul>
  </div>
  <div class="fcol" style="left:370px">
    <h5>SERVICES</h5>
    <ul><li>Air Injection/Irrigation</li><li>Alpha-Chymotrypsin</li><li>Capsule Polishers</li><li>Chamber Maintainers</li><li>Cortex Extraction</li></ul>
  </div>
  <div class="fcol" style="left:595px">
    <h5>RESOURCES</h5>
    <ul><li>Our Team</li><li>Term of Use</li><li>Blogs &amp; News</li><li>Contact Us</li></ul>
  </div>
  <div class="fcol" style="left:784px">
    <h5>CONTACT US</h5>
    <address>
      418 Harrowfield Lane Suite B20<br>Brookmere, PA 18055
      <div class="gap">(555) 014-2700<br>info@corvanta-medix.com</div>
    </address>
    <div class="socials">
      <span style="background:#45a8e0"></span>
      <span style="background:#2f5c9e"></span>
      <span style="background:#1f7bb0"></span>
      <span style="background:#d9503f"></span>
    </div>
  </div>
</footer>
<div class="abs footer-rule"></div>
<div class="abs copyright">© 2016 Company Name &nbsp;All right reserved &nbsp;Term of Use</div>

</body>
</html>
```